Copper Meadow Add-on Tearsheet

We’re looking to update our add-on tear sheet so that it matches the design of our updated general tear sheet. I’ve attached the 2024 add-on tear sheet, which needs to be refreshed, as well as our current general tear sheet for reference. We’d like the updated version to maintain the formatting style of the 2024 layout while incorporating all of the new content provided in the excel spreadsheet.

Please feel free to design the layout as you see fit for the 17 active portfolio companies. The order should follow the sequence in the Excel file — Brisley at the top and Pivot Welcott at the bottom. It’s fine if this requires two pages (front and back), though ideally we’d like to keep it to one page if possible.

Let me know if you have any questions!

```html
<!DOCTYPE html>
<html lang="en">
<head>
<meta charset="utf-8">
<title>Copper Meadow Add-on Tearsheet</title>
<link href="https://fonts.googleapis.com/css2?family=Libre+Baskerville:wght@400;700&family=Poppins:wght@300;400;600;800&display=swap" rel="stylesheet">
<style>
  :root{
    --stage:#1e1e1e;
    --paper:#ffffff;
    --navy:#22226b;
    --blue:#0b78c2;
    --band:#0a5fad;
    --row:#e4e5e9;
    --row-edge:#9aa0b5;
    --rule:#b9bcc4;
    --muted:#8a8a8a;
    --ink:#3a3a3a;
    --brand-green:#2e7d3a;
    --brand-blue:#1f6fb5;
    --label:#8c8c8c;
  }
  *{margin:0;padding:0;box-sizing:border-box}
  html,body{width:1200px;height:947px;overflow:hidden;background:var(--stage)}
  body{position:relative;font-family:'Poppins',sans-serif}
  .sheet{position:absolute;top:19px;width:559px;height:791px;background:var(--paper);overflow:hidden}
  .sheet--front{left:28px}
  .sheet--back{left:616px}
  .masthead{position:absolute;left:0;top:0;width:559px;height:84px}
  .firm-mark{position:absolute;left:31px;top:60px;font-family:'Libre Baskerville',serif;font-size:16px;color:var(--navy);letter-spacing:.3px;white-space:nowrap}
  .firm-name{position:absolute;right:28px;top:13px;font-family:'Libre Baskerville',serif;font-size:15px;color:#fff;letter-spacing:.4px;white-space:nowrap}
  .tagline{position:absolute;right:28px;top:49px;font-family:'Poppins',sans-serif;font-weight:800;font-size:12.4px;color:#fff;white-space:nowrap}
  .doc-title{position:absolute;right:27px;top:90px;font-weight:800;font-size:12.2px;color:#8e8e8e;white-space:nowrap}
  .title-rule{position:absolute;left:0;top:116px;width:559px;height:2px;background:var(--rule)}
  .col-head{position:absolute;left:0;top:119px;width:559px;height:26px;background:var(--navy);padding-left:27px;display:flex}
  .col-head span{width:72.1px;margin-right:.8px;height:26px;background:var(--blue);color:#fff;font-weight:600;font-size:5.2px;line-height:6px;text-align:center;display:flex;align-items:center;justify-content:center;text-transform:uppercase}
  .rows{position:absolute;left:27px;top:160px;width:505px}
  .entry{height:52px;margin-bottom:8px;background:var(--row);border:.6px solid var(--row-edge);display:flex;padding:5px 0}
  .entry div{width:72.1px;border-left:.6px dashed #9a9a9a;font-size:2.6px;line-height:3px;color:var(--ink);padding:0 5px;display:flex;align-items:center}
  .entry div:first-child{border-left:none;justify-content:center}
  .entry .size{justify-content:center}
  .entry .mix{font-size:2.4px;line-height:2.8px}
  .portco{font-size:6px;line-height:7px;font-weight:600;letter-spacing:.2px}
  .portco--brisley{color:var(--brand-green)}
  .portco--shoreline{color:var(--brand-blue)}
  .footer-band{position:absolute;left:0;top:702px;width:559px;height:8px;background:var(--band)}
  .contacts{position:absolute;left:0;top:730px;width:559px;display:flex}
  .contact{width:186.33px;text-align:center;font-weight:300;font-size:7.6px;line-height:8.5px;color:var(--muted)}
  .page-rule{position:absolute;left:0;top:780px;width:559px;height:.7px;background:var(--rule)}
  .page-num{position:absolute;left:273px;top:774px;width:13px;height:13px;border:.8px solid var(--blue);border-radius:50%;background:#fff;font-size:5px;font-weight:600;color:var(--blue);display:flex;align-items:center;justify-content:center}
  .page-label{position:absolute;top:852px;font-weight:300;font-size:24px;color:var(--label);letter-spacing:14px;white-space:nowrap}
  .page-label--front{left:208px}
  .page-label--back{left:793px}
</style>
</head>
<body>

<section class="sheet sheet--front">
  <svg class="masthead" viewBox="0 0 559 84">
    <polygon points="185,0 559,0 559,42 204,42" fill="#22226b"/>
    <polygon points="204,42 559,42 559,84 214,84" fill="#0b78c2"/>
    <polyline points="191,0 212,42 222,78 559,78" fill="none" stroke="#22226b" stroke-width=".8"/>
  </svg>
  <div class="firm-mark">COPPER MEADOW</div>
  <div class="firm-name">COPPER MEADOW CAPITAL PARTNERS</div>
  <div class="tagline">Investor Operators for the Lower Middle-Market</div>
  <div class="doc-title">Portfolio Company Add-on Acquisition Criteria</div>
  <div class="title-rule"></div>
  <div class="col-head"><span>Portco</span><span>Description</span><span>Size</span><span>Geography</span><span>End Markets /<br>Customers Served</span><span>Products / Services<br>/ Channels</span><span>Additional<br>Criteria</span></div>
  <div class="rows">
    <div class="entry"><div><span class="portco portco--brisley">Brisley</span></div><div>Premium residential landscape design, install, and maintenance service provider</div><div class="size">+5M rev</div><div>Priority: VA, MD, DE (DMV) and surrounding states</div><div>High net worth residential customers. Premium brands Maintenance and Enhancement focused</div><div class="mix">+80% Residential. Note: Home Owners Associations are considered commercial. +50% Maintenance means a 12-month contract to do routine landscape maintenance. &lt;10% New Construction Project work installing landscaping for a newly built home</div><div></div></div>
    <div class="entry"><div><span class="portco portco--brisley">Brisley</span></div><div>Premium residential landscape design, install, and maintenance service provider</div><div class="size">+5M rev</div><div>Priority: VA, MD, DE (DMV) and surrounding states</div><div>High net worth residential customers. Premium brands Maintenance and Enhancement focused</div><div class="mix">+80% Residential. Note: Home Owners Associations are considered commercial. +50% Maintenance means a 12-month contract to do routine landscape maintenance. &lt;10% New Construction Project work installing landscaping for a newly built home</div><div></div></div>
    <div class="entry"><div><span class="portco portco--brisley">Brisley</span></div><div>Premium residential landscape design, install, and maintenance service provider</div><div class="size">+5M rev</div><div>Priority: VA, MD, DE (DMV) and surrounding states</div><div>High net worth residential customers. Premium brands Maintenance and Enhancement focused</div><div class="mix">+80% Residential. Note: Home Owners Associations are considered commercial. +50% Maintenance means a 12-month contract to do routine landscape maintenance. &lt;10% New Construction Project work installing landscaping for a newly built home</div><div></div></div>
    <div class="entry"><div><span class="portco portco--brisley">Brisley</span></div><div>Premium residential landscape design, install, and maintenance service provider</div><div class="size">+5M rev</div><div>Priority: VA, MD, DE (DMV) and surrounding states</div><div>High net worth residential customers. Premium brands Maintenance and Enhancement focused</div><div class="mix">+80% Residential. Note: Home Owners Associations are considered commercial. +50% Maintenance means a 12-month contract to do routine landscape maintenance. &lt;10% New Construction Project work installing landscaping for a newly built home</div><div></div></div>
    <div class="entry"><div><span class="portco portco--brisley">Brisley</span></div><div>Premium residential landscape design, install, and maintenance service provider</div><div class="size">+5M rev</div><div>Priority: VA, MD, DE (DMV) and surrounding states</div><div>High net worth residential customers. Premium brands Maintenance and Enhancement focused</div><div class="mix">+80% Residential. Note: Home Owners Associations are considered commercial. +50% Maintenance means a 12-month contract to do routine landscape maintenance. &lt;10% New Construction Project work installing landscaping for a newly built home</div><div></div></div>
    <div class="entry"><div><span class="portco portco--brisley">Brisley</span></div><div>Premium residential landscape design, install, and maintenance service provider</div><div class="size">+5M rev</div><div>Priority: VA, MD, DE (DMV) and surrounding states</div><div>High net worth residential customers. Premium brands Maintenance and Enhancement focused</div><div class="mix">+80% Residential. Note: Home Owners Associations are considered commercial. +50% Maintenance means a 12-month contract to do routine landscape maintenance. &lt;10% New Construction Project work installing landscaping for a newly built home</div><div></div></div>
    <div class="entry"><div><span class="portco portco--brisley">Brisley</span></div><div>Premium residential landscape design, install, and maintenance service provider</div><div class="size">+5M rev</div><div>Priority: VA, MD, DE (DMV) and surrounding states</div><div>High net worth residential customers. Premium brands Maintenance and Enhancement focused</div><div class="mix">+80% Residential. Note: Home Owners Associations are considered commercial. +50% Maintenance means a 12-month contract to do routine landscape maintenance. &lt;10% New Construction Project work installing landscaping for a newly built home</div><div></div></div>
    <div class="entry"><div><span class="portco portco--brisley">Brisley</span></div><div>Premium residential landscape design, install, and maintenance service provider</div><div class="size">+5M rev</div><div>Priority: VA, MD, DE (DMV) and surrounding states</div><div>High net worth residential customers. Premium brands Maintenance and Enhancement focused</div><div class="mix">+80% Residential. Note: Home Owners Associations are considered commercial. +50% Maintenance means a 12-month contract to do routine landscape maintenance. &lt;10% New Construction Project work installing landscaping for a newly built home</div><div></div></div>
    <div class="entry"><div><span class="portco portco--brisley">Brisley</span></div><div>Premium residential landscape design, install, and maintenance service provider</div><div class="size"></div><div>Priority: VA, MD, DE (DMV) and surrounding states</div><div>High net worth residential customers. Premium brands Maintenance and Enhancement focused</div><div class="mix">+80% Residential. Note: Home Owners Associations are considered commercial. +50% Maintenance means a 12-month contract to do routine landscape maintenance. &lt;10% New Construction Project work installing landscaping for a newly built home</div><div></div></div>
  </div>
  <div class="footer-band"></div>
  <div class="contacts">
    <div class="contact">Dana Whitlock<br>Principal, Business Development<br>555-310-2041<br>dwhitlock@cm-cp.example</div>
    <div class="contact">Renee Halvorsen<br>Vice President, Business Development<br>555-310-2087<br>rhalvorsen@cm-cp.example</div>
    <div class="contact">Owen Castellano<br>Associate, Business Development<br>555-310-2093<br>ocastellano@cm-cp.example</div>
  </div>
  <div class="page-rule"></div>
  <div class="page-num">1</div>
</section>

<section class="sheet sheet--back">
  <svg class="masthead" viewBox="0 0 559 84">
    <polygon points="185,0 559,0 559,42 204,42" fill="#22226b"/>
    <polygon points="204,42 559,42 559,84 214,84" fill="#0b78c2"/>
    <polyline points="191,0 212,42 222,78 559,78" fill="none" stroke="#22226b" stroke-width=".8"/>
  </svg>
  <div class="firm-mark">COPPER MEADOW</div>
  <div class="firm-name">COPPER MEADOW CAPITAL PARTNERS</div>
  <div class="tagline">Investor Operators for the Lower Middle-Market</div>
  <div class="doc-title">Portfolio Company Add-on Acquisition Criteria</div>
  <div class="title-rule"></div>
  <div class="col-head"><span>Portco</span><span>Description</span><span>Size</span><span>Geography</span><span>End Markets /<br>Customers Served</span><span>Products / Services<br>/ Channels</span><span>Additional<br>Criteria</span></div>
  <div class="rows">
    <div class="entry"><div><span class="portco portco--shoreline">Shoreline</span></div><div>Premium residential landscape design, install, and maintenance service provider</div><div class="size">+5M rev</div><div>Priority: VA, MD, DE (DMV) and surrounding states</div><div>High net worth residential customers. Premium brands Maintenance and Enhancement focused</div><div class="mix">+80% Residential. Note: Home Owners Associations are considered commercial. +50% Maintenance means a 12-month contract to do routine landscape maintenance. &lt;10% New Construction Project work installing landscaping for a newly built home</div><div></div></div>
    <div class="entry"><div><span class="portco portco--shoreline">Shoreline</span></div><div>Premium residential landscape design, install, and maintenance service provider</div><div class="size">+5M rev</div><div>Priority: VA, MD, DE (DMV) and surrounding states</div><div>High net worth residential customers. Premium brands Maintenance and Enhancement focused</div><div class="mix">+80% Residential. Note: Home Owners Associations are considered commercial. +50% Maintenance means a 12-month contract to do routine landscape maintenance. &lt;10% New Construction Project work installing landscaping for a newly built home</div><div></div></div>
    <div class="entry"><div><span class="portco portco--shoreline">Shoreline</span></div><div>Premium residential landscape design, install, and maintenance service provider</div><div class="size">+5M rev</div><div>Priority: VA, MD, DE (DMV) and surrounding states</div><div>High net worth residential customers. Premium brands Maintenance and Enhancement focused</div><div class="mix">+80% Residential. Note: Home Owners Associations are considered commercial. +50% Maintenance means a 12-month contract to do routine landscape maintenance. &lt;10% New Construction Project work installing landscaping for a newly built home</div><div></div></div>
    <div class="entry"><div><span class="portco portco--shoreline">Shoreline</span></div><div>Premium residential landscape design, install, and maintenance service provider</div><div class="size">+5M rev</div><div>Priority: VA, MD, DE (DMV) and surrounding states</div><div>High net worth residential customers. Premium brands Maintenance and Enhancement focused</div><div class="mix">+80% Residential. Note: Home Owners Associations are considered commercial. +50% Maintenance means a 12-month contract to do routine landscape maintenance. &lt;10% New Construction Project work installing landscaping for a newly built home</div><div></div></div>
    <div class="entry"><div><span class="portco portco--shoreline">Shoreline</span></div><div>Premium residential landscape design, install, and maintenance service provider</div><div class="size">+5M rev</div><div>Priority: VA, MD, DE (DMV) and surrounding states</div><div>High net worth residential customers. Premium brands Maintenance and Enhancement focused</div><div class="mix">+80% Residential. Note: Home Owners Associations are considered commercial. +50% Maintenance means a 12-month contract to do routine landscape maintenance. &lt;10% New Construction Project work installing landscaping for a newly built home</div><div></div></div>
    <div class="entry"><div><span class="portco portco--shoreline">Shoreline</span></div><div>Premium residential landscape design, install, and maintenance service provider</div><div class="size">+5M rev</div><div>Priority: VA, MD, DE (DMV) and surrounding states</div><div>High net worth residential customers. Premium brands Maintenance and Enhancement focused</div><div class="mix">+80% Residential. Note: Home Owners Associations are considered commercial. +50% Maintenance means a 12-month contract to do routine landscape maintenance. &lt;10% New Construction Project work installing landscaping for a newly built home</div><div></div></div>
    <div class="entry"><div><span class="portco portco--shoreline">Shoreline</span></div><div>Premium residential landscape design, install, and maintenance service provider</div><div class="size">+5M rev</div><div>Priority: VA, MD, DE (DMV) and surrounding states</div><div>High net worth residential customers. Premium brands Maintenance and Enhancement focused</div><div class="mix">+80% Residential. Note: Home Owners Associations are considered commercial. +50% Maintenance means a 12-month contract to do routine landscape maintenance. &lt;10% New Construction Project work installing landscaping for a newly built home</div><div></div></div>
    <div class="entry"><div><span class="portco portco--shoreline">Shoreline</span></div><div>Premium residential landscape design, install, and maintenance service provider</div><div class="size">+5M rev</div><div>Priority: VA, MD, DE (DMV) and surrounding states</div><div>High net worth residential customers. Premium brands Maintenance and Enhancement focused</div><div class="mix">+80% Residential. Note: Home Owners Associations are considered commercial. +50% Maintenance means a 12-month contract to do routine landscape maintenance. &lt;10% New Construction Project work installing landscaping for a newly built home</div><div></div></div>
    <div class="entry"><div><span class="portco portco--shoreline">Shoreline</span></div><div>Premium residential landscape design, install, and maintenance service provider</div><div class="size"></div><div>Priority: VA, MD, DE (DMV) and surrounding states</div><div>High net worth residential customers. Premium brands Maintenance and Enhancement focused</div><div class="mix">+80% Residential. Note: Home Owners Associations are considered commercial. +50% Maintenance means a 12-month contract to do routine landscape maintenance. &lt;10% New Construction Project work installing landscaping for a newly built home</div><div></div></div>
  </div>
  <div class="footer-band"></div>
  <div class="contacts">
    <div class="contact">Dana Whitlock<br>Principal, Business Development<br>555-310-2041<br>dwhitlock@cm-cp.example</div>
    <div class="contact">Renee Halvorsen<br>Vice President, Business Development<br>555-310-2087<br>rhalvorsen@cm-cp.example</div>
    <div class="contact">Owen Castellano<br>Associate, Business Development<br>555-310-2093<br>ocastellano@cm-cp.example</div>
  </div>
  <div class="page-rule"></div>
  <div class="page-num">2</div>
</section>

<div class="page-label page-label--front">page 01</div>
<div class="page-label page-label--back">page 02</div>

</body>
</html>
```